PALS postcard design

We need a design for a non profit organization associated with an animal shelter called PALS of NHRPC. NHRPC stands for Northbrook Hollow Regional Pet Center. This 501c3 group provides assistance to the community in the form of training, consultation, financial assistance, education and more. Our goal is to provide options to people in need to help them keep their pets rather than surrender them to the shelter. We have a logo already but we need something for people to take away and to use as a handout. Need to include phone numbers and website, which I will provide.

Target Market(s)

general public who have pets

Industry/Entity Type

Non Profit

Font styles to use
Sans Serif
Other font styles liked:
• designer can choose others

Requirements
Must have
• The logo must be fairly large. Colors should be bright and eye-pleasing. Like colors that match the logo. Easy to read fonts. Pics of animals are OK but no pics with people. Not too much text, short and to the point.
Nice to have
• not sure
Should not have
• No pics with people. Not black and white. Not too much text.

```html
<!DOCTYPE html>
<html lang="en">
<head>
<meta charset="utf-8">
<title>PALS of NHRPC Postcard</title>
<link rel="stylesheet" href="https://fonts.googleapis.com/css2?family=Oswald:wght@700&family=Roboto+Condensed:wght@700&family=Montserrat:wght@600;700&display=swap">
<style>
  :root {
    --backdrop: #e9e4dc;
    --cyan: #29c2e6;
    --yellow: #f7ec13;
    --red: #ee4036;
    --white: #ffffff;
    --divider: #3fb7d9;
  }
  * { box-sizing: border-box; margin: 0; padding: 0; }
  html, body {
    width: 1200px; height: 960px; overflow: hidden;
    background: var(--backdrop);
  }
  .stage { position: relative; width: 1200px; height: 960px; }
  .postcard {
    position: absolute; left: 119px; top: 216px;
    width: 1200px; height: 660px;
    transform: scale(0.8); transform-origin: top left;
    background: var(--cyan);
    box-shadow: 0 6px 18px rgba(0,0,0,0.25);
    overflow: hidden;
  }
  .brand {
    position: absolute; left: 40px; top: 388px; width: 330px;
    display: flex; align-items: center; justify-content: center; gap: 12px;
  }
  .brand-dot { width: 24px; height: 24px; border-radius: 50%; background: var(--red); flex: none; }
  .brand-name {
    font-family: "Roboto Condensed", sans-serif; font-weight: 700;
    font-size: 40px; color: var(--red); letter-spacing: 1px; white-space: nowrap;
  }
  .web-bar {
    position: absolute; left: 0; top: 549px; width: 370px; height: 78px;
    background: var(--red); color: var(--white);
    font-family: "Montserrat", sans-serif; text-align: right;
    padding: 16px 17px 0 0;
  }
  .web-bar .label { font-weight: 700; font-size: 15px; white-space: nowrap; }
  .web-bar .url { font-weight: 600; font-size: 23px; letter-spacing: 1px; line-height: 1.2; white-space: nowrap; }
  .message { position: absolute; left: 403px; top: 44px; width: 450px; }
  .headline {
    font-family: "Oswald", sans-serif; font-weight: 700;
    font-size: 42px; line-height: 58px; color: var(--yellow);
    text-transform: uppercase; letter-spacing: -0.5px; white-space: nowrap;
  }
  .body-copy {
    margin-top: 18px;
    font-family: "Roboto Condensed", sans-serif; font-weight: 700;
    font-size: 18px; line-height: 25.8px; color: var(--white);
  }
  .call {
    position: absolute; left: 404px; top: 556px;
    font-family: "Montserrat", sans-serif; font-weight: 700;
    color: var(--yellow); text-transform: uppercase;
    font-size: 26px; line-height: 32px; white-space: nowrap;
  }
  .call .phone { font-size: 35px; }
  .side { position: absolute; left: 904px; top: 0; width: 296px; height: 660px; background: var(--divider); }
  .photo { position: absolute; left: 0; width: 296px; }
  .photo-dog { top: 0; height: 202px; background: linear-gradient(160deg, #8fae78 0%, #4d7a3a 55%, #dcdad3 75%, #3f6a2f 100%); }
  .photo-cat { top: 459px; height: 201px; background: linear-gradient(170deg, #8a6a52 0%, #b89278 45%, #d9c9bb 70%, #a77f5f 100%); }
  .help {
    position: absolute; left: 0; top: 208px; width: 296px; height: 245px;
    background: var(--red); padding: 16px 16px 0 16px; color: var(--white);
    font-family: "Roboto Condensed", sans-serif; font-weight: 700;
  }
  .help h2 {
    font-family: "Oswald", sans-serif; font-weight: 700;
    font-size: 27px; color: var(--yellow); text-transform: uppercase; line-height: 34px;
    margin-bottom: 6px; white-space: nowrap;
  }
  .help p { font-size: 16px; line-height: 20px; margin-bottom: 20px; }
</style>
</head>
<body>
<div class="stage">
  <section class="postcard">
    <div class="brand">
      <span class="brand-dot"></span>
      <span class="brand-name">PALS of NHRPC</span>
    </div>

    <div class="web-bar">
      <div class="label">Visit Our Website For More information</div>
      <div class="url">www.palsofnhrpc.org</div>
    </div>

    <div class="message">
      <h1 class="headline">Supporting the shelter<br>in their goal to create<br>a no-kill community</h1>
      <p class="body-copy">Pals of Northbrook Hollow Regional Pet Center is an integral part of Northbrook’s lifesaving mission. We provide behavioral enrichment programs for adopted dogs and are in the process of creating an assistance program for families who are experiencing financial troubles due to animal related expenses such as pet deposits or medical costs. We will also offer free training consults, both in the home and at the shelter, for those who need it. Our focus is to create second chances for families who think their only solution is surrendering a pet to a shelter or simply abandoning them.</p>
    </div>

    <div class="call">If you need any assistance<br>please call <span class="phone">555-014-0754</span></div>

    <aside class="side">
      <div class="photo photo-dog" role="img" aria-label="Photo of a happy small white terrier standing on grass"></div>
      <div class="help">
        <h2>How can you help?</h2>
        <p>Volunteers are needed for fundraising, program and volunteer committees. Plus hands on work at the shelter!.</p>
        <p>Donations will support our continuing education, community outreach and intervention programs.</p>
      </div>
      <div class="photo photo-cat" role="img" aria-label="Photo of a tabby and white cat crouching on a wooden floor"></div>
    </aside>
  </section>
</div>
</body>
</html>
```